Business card for event manager / organizer "velmora tandem"

Draft of a new valuable business card for my company.
Events, personnel service providers, festivals

```html
<!DOCTYPE html>
<html lang="de">
<head>
<meta charset="utf-8">
<title>velmora tandem – Visitenkarte</title>
<link href="https://fonts.googleapis.com/css2?family=Roboto:wght@300;400;700&display=swap" rel="stylesheet">
<style>
  :root {
    --stage: #2c2c30;
    --card-dark: #050505;
    --card-light: #ffffff;
    --accent: #f07f1c;
    --ink-light: #ffffff;
    --ink-dark: #111111;
    --photo-a: #3a3a3e;
    --photo-b: #0c0c0c;
  }
  * { margin: 0; padding: 0; box-sizing: border-box; }
  html, body { width: 1200px; height: 913px; overflow: hidden; }
  body {
    background: var(--stage);
    font-family: "Roboto", Arial, sans-serif;
    position: relative;
  }
  .card {
    position: absolute;
    width: 540px;
    height: 330px;
    border-radius: 18px;
    border-bottom: 3px solid var(--accent);
    overflow: hidden;
  }
  .card--front { left: 50px; top: 110px; background: var(--card-dark); color: var(--ink-light); }
  .card--back  { left: 610px; top: 473px; background: var(--card-light); color: var(--ink-dark); }

  .portrait {
    position: absolute;
    left: 0; bottom: 0;
    width: 225px; height: 300px;
    background: radial-gradient(ellipse at 50% 35%, var(--photo-a), var(--photo-b) 75%);
  }

  .brand { display: flex; align-items: center; gap: 10px; white-space: nowrap; }
  .brand__mark { width: 34px; height: 34px; background: var(--accent); flex: none; }
  .brand__name { font-weight: 700; font-size: 30px; letter-spacing: 0.5px; line-height: 1; color: var(--ink-light); }

  .card--front .brand { position: absolute; left: 250px; top: 36px; }

  .person { position: absolute; left: 250px; top: 112px; }
  .person__name { color: var(--accent); font-size: 26px; font-weight: 400; letter-spacing: 0.5px; }
  .person__role { font-size: 13px; font-weight: 400; margin-top: 2px; letter-spacing: 0.5px; }

  .contact { position: absolute; left: 250px; top: 182px; list-style: none; }
  .contact li { display: flex; align-items: center; gap: 8px; font-size: 13px; line-height: 20px; white-space: nowrap; }
  .contact svg { width: 11px; height: 11px; flex: none; fill: none; stroke: var(--accent); stroke-width: 2; }
  .contact .dot { width: 10px; height: 10px; border-radius: 50%; background: var(--accent); flex: none; }

  .card--back .brand {
    position: absolute; left: 50%; top: 50%;
    transform: translate(-50%, -50%);
    gap: 14px;
  }
  .card--back .brand__mark { width: 56px; height: 56px; }
  .card--back .brand__name { font-size: 48px; color: var(--ink-dark); }
</style>
</head>
<body>

  <section class="card card--front">
    <div class="portrait" role="img" aria-label="Porträtfoto eines Kellners mit Fliege und Tablett mit Sektgläsern"></div>

    <div class="brand">
      <span class="brand__mark"></span>
      <span class="brand__name">velmora tandem</span>
    </div>

    <div class="person">
      <h1 class="person__name">LUKAS ARNHOLD</h1>
      <p class="person__role">INHABER</p>
    </div>

    <ul class="contact">
      <li><svg viewBox="0 0 12 12"><path d="M3 1 L5 3.5 L4 5 Q5.5 7 7 8 L8.5 7 L11 9 L9.5 11 Q4 10 1 2.5 Z"/></svg>02361 555 01 42</li>
      <li><svg viewBox="0 0 12 12"><path d="M3 1 L5 3.5 L4 5 Q5.5 7 7 8 L8.5 7 L11 9 L9.5 11 Q4 10 1 2.5 Z"/></svg>0170 555 27 39</li>
      <li><svg viewBox="0 0 12 12"><rect x="1" y="2.5" width="10" height="7"/><path d="M1 2.5 L6 6.5 L11 2.5"/></svg>info@velmora-tandem.de</li>
      <li><svg viewBox="0 0 12 12"><circle cx="6" cy="6" r="5"/><path d="M1 6 H11 M6 1 Q3 6 6 11 M6 1 Q9 6 6 11"/></svg>www.velmora-tandem.de</li>
      <li><svg viewBox="0 0 12 12"><path d="M6 11 Q2 6.5 2 4.5 A4 4 0 0 1 10 4.5 Q10 6.5 6 11 Z"/><circle cx="6" cy="4.5" r="1.3"/></svg>Lindenweg 14, 45699 Herten</li>
      <li><span class="dot"></span>www.velmora-tandem.de/team</li>
    </ul>
  </section>

  <section class="card card--back">
    <div class="brand">
      <span class="brand__mark"></span>
      <span class="brand__name">velmora tandem</span>
    </div>
  </section>

</body>
</html>
```